Business Card for By Karel Voss

Looking to have a business card designed for my lifestyle and fitness company. My company offers personal training, online programming and nutrition advice based out of London, United Kingdom.

I'd like to see modern, sleek designs, focusing on black, matte black or matte grey. Design doesn't need to be overly descriptive as this will also be used as a personal business card. I've included my logo.

Please note that my company is no longer called "Fitness by Karel Voss" but instead "By Karel Voss", this is because of my other ventures. Therefore please don't use the "fitness by karel voss" text.

information about my company can be found at www.bykarelvoss.com

Company is also based out of London (United Kingdom) & Sydney (Australia) this could be reflected on the card.

Industry/Entity Type

Business

Contact Information for Business Card

Karel Voss
+44 7382 615027
karel@bykarelvoss.com
www.bykarelvoss.com

Font styles to use
Sans Serif

Requirements
Must have
• All contact details and inclusion of my logo.

```html
<!DOCTYPE html>
<html lang="en">
<head>
<meta charset="utf-8">
<title>By Karel Voss – Business Card</title>
<link rel="stylesheet" href="https://fonts.googleapis.com/css2?family=Roboto:wght@300;400;700&display=swap">
<style>
  :root {
    --backdrop: #e4e1dc;
    --card-white: #f4f4f3;
    --card-black: #1a1a1b;
    --card-black-soft: #2a2a2c;
    --stripe-grey: #4a4a4c;
    --ink-dark: #1d1d1f;
    --ink-light: #e9e9ea;
    --ink-muted: #a9a9ad;
  }
  * { box-sizing: border-box; margin: 0; padding: 0; }
  html, body {
    width: 1200px; height: 1023px; overflow: hidden;
    background: var(--backdrop);
    font-family: "Roboto", Arial, sans-serif;
  }
  .canvas { position: relative; width: 1200px; height: 1023px; }
  .card {
    position: absolute; left: 220px; width: 760px; height: 434px;
    overflow: hidden; border-radius: 4px;
    box-shadow: 0 10px 28px rgba(0,0,0,.22);
  }
  .card--front { top: 60px; background: var(--card-white); }
  .card--back { top: 530px; background: linear-gradient(160deg, var(--card-black-soft), var(--card-black)); }
  .card svg.shapes { position: absolute; inset: 0; }
  .brand {
    position: absolute; left: 56px; top: 116px;
    display: flex; align-items: center; gap: 16px;
  }
  .brand__dot { width: 44px; height: 44px; border-radius: 50%; background: var(--ink-dark); }
  .brand__name {
    font-weight: 700; font-size: 40px; letter-spacing: 2px;
    text-transform: uppercase; color: var(--ink-dark);
  }
  .contact {
    position: absolute; left: 48px; top: 282px; color: var(--ink-light);
  }
  .contact__name { font-size: 30px; font-weight: 300; }
  .contact__role { font-size: 12px; color: var(--ink-muted); margin-top: 2px; margin-bottom: 16px; }
  .contact__line {
    display: flex; align-items: center; gap: 12px;
    font-size: 17px; font-weight: 400; margin-top: 8px;
  }
  .contact__line svg { width: 16px; height: 16px; flex: none; }
  .back-mark {
    position: absolute; left: 50%; top: 50%; width: 240px; height: 240px;
    transform: translate(-50%, -50%); border-radius: 50%;
    border: 10px solid rgba(255,255,255,.05);
  }
</style>
</head>
<body>
<main class="canvas">
  <section class="card card--front" aria-label="Business card front">
    <svg class="shapes" viewBox="0 0 760 434" width="760" height="434" aria-hidden="true">
      <defs>
        <linearGradient id="panelGloss" x1="0" y1="0" x2="1" y2="1">
          <stop offset="0" stop-color="#2e2e30"/>
          <stop offset="1" stop-color="#141415"/>
        </linearGradient>
      </defs>
      <path d="M470 150 L760 150 L760 166 L486 166 Q476 166 470 158 Z" fill="var(--stripe-grey)"/>
      <path d="M0 262 L400 262 Q440 262 456 222 Q468 186 510 186 L760 186 L760 434 L0 434 Z" fill="url(#panelGloss)"/>
    </svg>

    <div class="brand">
      <span class="brand__dot"></span>
      <span class="brand__name">By Karel Voss</span>
    </div>

    <div class="contact">
      <p class="contact__name">Karel Voss</p>
      <p class="contact__role">Director</p>
      <p class="contact__line">
        <svg viewBox="0 0 16 16"><path d="M3.5 1.5l2.5 0 1 3.5-1.8 1.2a8 8 0 0 0 4.6 4.6L11 9l3.5 1v2.5c0 1-1 2-2 2A11 11 0 0 1 1.5 3.5c0-1 1-2 2-2z" fill="currentColor"/></svg>
        +44 7382 615027
      </p>
      <p class="contact__line">
        <svg viewBox="0 0 16 16"><rect x="1.5" y="3.5" width="13" height="9" fill="none" stroke="currentColor" stroke-width="1.4"/><path d="M1.5 3.5 8 9l6.5-5.5" fill="none" stroke="currentColor" stroke-width="1.4"/></svg>
        karel@bykarelvoss.com
      </p>
      <p class="contact__line">
        <svg viewBox="0 0 16 16"><circle cx="8" cy="8" r="6.5" fill="none" stroke="currentColor" stroke-width="1.4"/><path d="M1.5 8h13M8 1.5c-3 3.5-3 9.5 0 13M8 1.5c3 3.5 3 9.5 0 13" fill="none" stroke="currentColor" stroke-width="1.2"/></svg>
        www.bykarelvoss.com
      </p>
    </div>
  </section>

  <section class="card card--back" aria-label="Business card back">
    <span class="back-mark"></span>
  </section>
</main>
</body>
</html>
```